Business Card for IT company

I need a high tech looking business card using our logo. I prefer something clean and modern.

Target Market(s)

Buyers of IT hardware and software, IT Techies who are key influencers

Industry/Entity Type

Business

```html
<!DOCTYPE html>
<html lang="en">
<head>
<meta charset="utf-8">
<title>Brightvale Consulting – Business Card</title>
<link rel="stylesheet" href="https://fonts.googleapis.com/css2?family=Fira+Sans:wght@400;500;600&display=swap">
<style>
  :root {
    --backdrop: #bdbdbd;
    --card-white: #ffffff;
    --card-white-shade: #f1f1f1;
    --ink: #2b2b2b;
    --ink-soft: #3a3a3a;
    --brand-green: #3c9a2e;
    --green-deep: #2e9237;
    --green-mid: #5db52e;
    --green-light: #9fd66a;
  }
  * { box-sizing: border-box; margin: 0; padding: 0; }
  html, body {
    width: 1200px;
    height: 960px;
    overflow: hidden;
    background: var(--backdrop);
    font-family: "Fira Sans", Arial, sans-serif;
  }
  .canvas {
    position: relative;
    width: 1200px;
    height: 960px;
  }
  .card {
    position: absolute;
    left: 267px;
    width: 665px;
    height: 380px;
    overflow: hidden;
    box-shadow: 0 10px 28px rgba(0,0,0,0.22);
  }
  .card--front {
    top: 66px;
    background: linear-gradient(160deg, var(--card-white) 40%, var(--card-white-shade) 100%);
  }
  .card--back {
    top: 514px;
    background: linear-gradient(120deg, var(--green-deep) 0%, var(--green-mid) 55%, var(--green-light) 100%);
  }
  .trace-glow {
    position: absolute;
  }
  .card--front .trace-glow {
    right: 0;
    bottom: 0;
    width: 330px;
    height: 190px;
    background: radial-gradient(ellipse at 70% 60%, rgba(225,230,235,0.9) 0%, rgba(240,242,244,0.4) 50%, rgba(255,255,255,0) 80%);
  }
  .card--back .trace-glow {
    left: 0;
    top: 0;
    width: 100%;
    height: 100%;
    background: radial-gradient(ellipse at 45% 35%, rgba(255,255,255,0.28) 0%, rgba(255,255,255,0) 55%);
  }
  .holder-name {
    position: absolute;
    left: 56px;
    top: 64px;
    font-size: 34px;
    line-height: 40px;
    font-weight: 600;
    color: var(--ink);
    letter-spacing: -0.3px;
  }
  .holder-role {
    position: absolute;
    left: 57px;
    top: 106px;
    font-size: 21px;
    line-height: 26px;
    color: var(--brand-green);
  }
  .contact {
    position: absolute;
    left: 58px;
    top: 190px;
    font-size: 17px;
    line-height: 21px;
    font-style: normal;
    color: var(--ink-soft);
  }
  .contact .company { color: var(--brand-green); margin-bottom: 4px; }
  .contact .address { margin-bottom: 4px; }
  .contact .label { color: var(--brand-green); }
  .contact .web {
    margin-top: 6px;
    font-weight: 600;
    font-size: 18px;
    line-height: 22px;
    color: var(--ink);
    letter-spacing: 0.3px;
  }
  .wordmark {
    position: absolute;
    font-weight: 500;
    color: var(--ink);
    font-size: 44px;
    line-height: 52px;
    letter-spacing: -0.5px;
    white-space: nowrap;
  }
  .card--front .wordmark { right: 44px; top: 120px; }
  .card--back .wordmark { right: 40px; bottom: 92px; }
</style>
</head>
<body>
  <main class="canvas">
    <section class="card card--front" aria-label="Business card front">
      <div class="trace-glow" role="img" aria-label="Faint glowing circuit trace lines"></div>
      <h1 class="holder-name">Your Name</h1>
      <p class="holder-role">Your Designation</p>
      <div class="wordmark">Brightvale</div>
      <address class="contact">
        <div class="company">Brightvale Consulting, LLC.</div>
        <div class="address">420 Meridian Parkway<br>Suite 800<br>Fairview, VA 22150</div>
        <div><span class="label">Main Reception:</span> 555.210.4480</div>
        <div><span class="label">Office Manager:</span> 555.210.4482/4483</div>
        <div class="web">www.brightvale.example</div>
      </address>
    </section>

    <section class="card card--back" aria-label="Business card back">
      <div class="trace-glow" role="img" aria-label="Glowing white circuit trace lines across green background"></div>
      <div class="wordmark">Brightvale</div>
    </section>
  </main>
</body>
</html>
```